Global Beard Oil Review Business needs a refresh

topwhiskerbalm.net is a global business who's mission is to curate all available beard oils from around the world, review and grade them and present this curated collection to the user of the website.

The scope of this job includes the web site design and the design of a suitable logo to be used in the site header.

The existing site can be seen on http://topwhiskerbalm.net, however this is a mock-up only the style and logo should NOT be used. This is to give you an idea of the concept of the site only.

This job is for PSD design only.

See attached design brief for detailed design requirements.
Updates

Target Market(s)

Men's grooming / retail

Industry/Entity Type

Retail

Number of Pages Required

2 page

Font styles to use
Sans Serif

Requirements
Must have
• 1) Comparison Table
• 2) Side Bar
• 3) Header area
• 4) Photo of Lomax Penhallow (attached - can be circular or "cut-out")
• 5) Cool beard-oriented custom design background (e.g., stylistic black/brown on brown/orange beard background. I envision this beard background "drawing" rather than photo based)
• (see attached design requirements for details)
Nice to have
• Signature style writing at top with name "Lomax Penhallow"
Should not have
• Do NOT use the look & feel or logo from the existing site.

```html
<!DOCTYPE html>
<html lang="en">
<head>
<meta charset="utf-8">
<title>Top Whisker Balm — Global Beard Oil Review</title>
<link href="https://fonts.googleapis.com/css2?family=Open+Sans:wght@400;600;700&family=PT+Sans:wght@400;700&display=swap" rel="stylesheet">
<style>
:root{
  --hair-dark:#3a1a0c;
  --hair-mid:#8a4426;
  --hair-light:#c07a55;
  --band:#2a120a;
  --accent:#5a2204;
  --accent-deep:#320f02;
  --panel:#ece6e3;
  --row-a:#ddd5d2;
  --row-b:#c9c0bd;
  --link:#6b3300;
  --ink:#111;
  --white:#fff;
}
*{box-sizing:border-box;margin:0;padding:0}
html,body{width:1200px;height:1000px;overflow:hidden}
body{
  position:relative;
  font-family:"PT Sans",sans-serif;color:var(--ink);
  background:
    repeating-linear-gradient(115deg,rgba(255,255,255,.05) 0 3px,rgba(0,0,0,.06) 3px 7px),
    linear-gradient(135deg,var(--hair-mid),var(--hair-light) 35%,var(--hair-mid) 60%,var(--hair-dark));
}
.logo{position:absolute;left:34px;top:0;width:206px;height:163px;background:rgba(40,16,6,.85);display:flex;flex-direction:column;align-items:center;justify-content:center;gap:10px}
.logo-mark{display:flex;align-items:center;gap:12px}
.logo-dot{width:20px;height:20px;border-radius:50%;background:#e3b48c}
.logo-name{font-family:"Open Sans",sans-serif;font-weight:700;font-size:22px;line-height:1.15;color:var(--white)}
.logo-url{font-family:"Open Sans",sans-serif;font-weight:700;font-size:16px;color:#c8894f}
.site-title{position:absolute;left:380px;top:56px;width:406px;text-align:center;font-family:"Open Sans",sans-serif;font-size:30px;line-height:36px;color:var(--white)}
.host-photo{position:absolute;left:944px;top:11px;width:226px;height:226px;border-radius:50%;border:8px solid #c9c9cc;box-shadow:0 0 0 2px #777;background:radial-gradient(circle at 45% 45%,#d8793e,#8a3a16 70%,#3a1a0c)}
.nav{position:absolute;left:0;top:183px;width:1200px;height:71px;background:rgba(30,12,6,.55);display:flex;padding-left:34px}
.nav a{color:var(--white);text-decoration:none;font-family:"Open Sans",sans-serif;font-weight:700;font-size:14px;display:flex;align-items:center;height:71px}
.nav a.active{width:154px;justify-content:center;background:linear-gradient(var(--accent),var(--accent-deep))}
.main{position:absolute;left:0;top:274px;width:900px;height:633px;background:rgba(236,230,227,.93)}
.main h1{font-family:"Open Sans",sans-serif;font-size:18px;font-weight:700;position:absolute;left:34px;top:18px}
.intro{position:absolute;left:48px;top:55px;width:840px;font-size:14px;line-height:16.5px}
.intro strong{display:block;margin-top:18px}
.reviews{position:absolute;left:0;top:152px;width:900px;border-collapse:collapse;table-layout:fixed}
.reviews th{height:67px;color:var(--white);font-size:14px;font-weight:700;background:linear-gradient(var(--accent),var(--accent-deep));border-left:1px solid #7a3a12}
.reviews th.light{font-weight:400}
.reviews th.hl{background:linear-gradient(#3a1404,#6a2c08)}
.reviews td{height:101px;border-top:1px solid #7a3a12;border-left:1px solid #7a3a12;font-size:14px;text-align:center;background:var(--row-a)}
.reviews tr:nth-child(even) td{background:var(--row-b)}
.reviews td.supplier,.reviews td.name{text-align:left;padding-left:6px;font-weight:700}
.reviews td.name{color:var(--link)}
.reviews td.origin{font-weight:700}
.reviews td.overall{color:var(--link);font-weight:700}
.reviews td.photo{padding:0}
.bottle{width:100%;height:100px;background:linear-gradient(#f4efe9,#d6b79a)}
.bottle.dark{background:linear-gradient(#e2c9ac,#3a2616)}
.buy{display:inline-block;background:linear-gradient(var(--accent),var(--accent-deep));color:var(--white);font-weight:700;font-size:14px;padding:10px 5px}
.sidebar{position:absolute;left:920px;top:274px;width:280px;height:726px;background:var(--white)}
.search{position:absolute;left:24px;top:14px;width:225px;height:39px;border:1px solid #6a3310;display:flex}
.search span{flex:1;padding:10px 12px;color:#999;font-weight:700;font-size:15px}
.search i{width:40px;background:var(--accent-deep);display:flex;align-items:center;justify-content:center}
.side-h{position:absolute;left:0;width:280px;height:39px;background:linear-gradient(var(--accent),var(--accent-deep));color:var(--white);font-family:"Open Sans",sans-serif;font-weight:700;font-size:18px;padding:6px 24px}
.side-list{position:absolute;left:25px;list-style:none;font-size:12px;font-weight:700}
.side-list a{color:var(--accent-deep)}
.side-list li{margin-bottom:13px;line-height:14px}
.product-shot{position:absolute;left:110px;top:541px;width:150px;height:160px;background:linear-gradient(90deg,#c4a07a 0 45%,#eee 45%)}
.footer{position:absolute;left:0;top:931px;width:920px;height:51px;background:rgba(30,12,6,.85);color:var(--white);font-weight:700;font-size:14px;padding:16px 34px}
</style>
</head>
<body>
<div class="logo">
  <div class="logo-mark"><span class="logo-dot"></span><span class="logo-name">Top<br>Whisker<br>Balm</span></div>
  <div class="logo-url">topwhiskerbalm.net</div>
</div>
<div class="site-title">Global Beard Oil Review<br>with Lomax Penhallow</div>
<div class="host-photo" role="img" aria-label="Photo of Lomax Penhallow giving a thumbs up and holding a beard oil bottle"></div>
<nav class="nav">
  <a class="active" href="#">Front page</a>
  <a href="#" style="margin-left:31px">About Me</a>
  <a href="#" style="margin-left:71px">Beard Oil Review Methodology</a>
  <a href="#" style="margin-left:90px">Charter</a>
  <a href="#" style="margin-left:88px">Blog</a>
</nav>
<main class="main">
  <h1>The World’s #1 Beard Oil Authority</h1>
  <p class="intro">Here is the master list of beard oils reviewed to date. You can link directly to the corresponding review by clicking on the name of the beard oil. In accordance with our charter, we are actively working to locate and review every single beard oil available on the planet Earth.<strong>Check back regularly for updates.</strong></p>
  <table class="reviews">
    <colgroup><col style="width:34px"><col style="width:89px"><col style="width:91px"><col style="width:101px"><col style="width:77px"><col style="width:91px"><col style="width:90px"><col style="width:52px"><col style="width:88px"><col style="width:46px"><col style="width:55px"><col style="width:86px"></colgroup>
    <tr><th></th><th>Supplier</th><th>Name</th><th>Photo</th><th class="hl">Origin</th><th>Base<br>Oil</th><th>Scent</th><th class="light">Aroma</th><th class="light">Therapeutic Affect</th><th class="light">Value</th><th class="light">Overall</th><th></th></tr>
    <tr><td></td><td class="supplier">Grizzled Goat</td><td class="name">Timberline</td><td class="photo"><div class="bottle" role="img" aria-label="Timberline beard oil bottle"></div></td><td class="origin">USA</td><td></td><td></td><td>0</td><td>0</td><td>0</td><td class="overall">0</td><td><span class="buy">Buy Now</span></td></tr>
    <tr><td></td><td class="supplier">Wholeself Suds</td><td class="name">Outbacker's Beard Oil</td><td class="photo"><div class="bottle" role="img" aria-label="Outbacker's beard oil dropper bottle"></div></td><td class="origin">Australia</td><td></td><td></td><td>0</td><td>0</td><td>0</td><td class="overall">0</td><td><span class="buy">Buy Now</span></td></tr>
    <tr><td></td><td class="supplier">Clipperfolk Men's Grooming</td><td class="name">Clipperfolk Beard Oil</td><td class="photo"><div class="bottle dark" role="img" aria-label="Clipperfolk beard oil dark bottle"></div></td><td class="origin">Australia</td><td></td><td></td><td>0</td><td>0</td><td>0</td><td class="overall">0</td><td><span class="buy">Buy Now</span></td></tr>
    <tr><td></td><td class="supplier">Uncle Rudd Grooming</td><td class="name">Misty Ridge Man Beard Oil</td><td class="photo"><div class="bottle" role="img" aria-label="Misty Ridge beard oil amber dropper bottle"></div></td><td class="origin">Australia</td><td></td><td></td><td>0</td><td>0</td><td>0</td><td class="overall">0</td><td><span class="buy">Buy Now</span></td></tr>
  </table>
</main>
<aside class="sidebar">
  <div class="search"><span>Search</span><i><svg width="20" height="20" viewBox="0 0 20 20"><circle cx="8" cy="8" r="5.5" fill="none" stroke="#fff" stroke-width="2.5"/><line x1="12" y1="12" x2="18" y2="18" stroke="#fff" stroke-width="3"/></svg></i></div>
  <div class="side-h" style="top:64px">Categories</div>
  <ul class="side-list" style="top:118px"><li><a href="#">Articles</a></li><li><a href="#">Reviews</a></li></ul>
  <div class="side-h" style="top:180px">Recent Posts</div>
  <ul class="side-list" style="top:233px">
    <li><a href="#">The Wandering Corsair Beard<br>Oil by Fernhollow Creations</a></li>
    <li><a href="#">Misty Ridge Man Beard<br>Oil by Uncle Rudd Grooming</a></li>
    <li><a href="#">Outbacker’s Face/Beard<br>Oil by Wholeself Suds</a></li>
    <li><a href="#">Clipperfolk Beard Oil<br>by Clipperfolk Men’s Grooming</a></li>
    <li><a href="#">Axeman Oil<br>by Allied Whisker Co.</a></li>
  </ul>
  <div class="side-h" style="top:447px">Archives</div>
  <ul class="side-list" style="top:511px"><li><a href="#">February 2016</a></li><li><a href="#">January 2016</a></li></ul>
  <div class="product-shot" role="img" aria-label="Beard oil bottle beside its kraft paper box"></div>
</aside>
<footer class="footer">Copyright © 2016 Top Whisker Balm. All rights reserved.</footer>
</body>
</html>
```